Training in Brief Tobacco Use Interventions

We need a design/template for an e-learning course. The course is being created for healthcare professionals. The template should include a home page (title), and subtitle page (introduction, chapter, test, help, references and so on). We would like to see designs that are very professional and appealling.

Reason: Can you extend deadline. I have not heard back from designers.

Target Market(s)

Healthcare professionals

Industry/Entity Type

Health Care

Number of Pages Required

4 page

Font styles to use
Sans Serif

Colors
3276b5
85acd3
ffc214
f37122
ffcf3e
886aae
acd136

Requirements
Must have
• The project's title page should be very professional and appealing for a very serious audience. The title page should include an image of healthcare provider, and/or no smoking symbol.
Nice to have
• Pages should include icons such as next and previous buttons, along with progress status bar on bottom of design. Also should include top row containing for primary chapters. In addition, left side of page should contain space for detailed table of contents and additional resources.
Should not have
• Design should not appear cluttered or confusing. Large space for logo.

```html
<!DOCTYPE html>
<html lang="en">
<head>
<meta charset="utf-8">
<title>Brief Tobacco Use Interventions – Case Scenarios</title>
<link href="https://fonts.googleapis.com/css2?family=Alegreya+Sans:wght@300;400;500;700&display=swap" rel="stylesheet">
<style>
:root{
  --orange:#f37122;
  --blue:#3276b5;
  --green:#acd136;
  --purple:#886aae;
  --yellow:#ffc214;
  --dark:#2f2c2c;
  --darker:#3b3939;
  --light:#efefef;
  --text:#444;
  --white:#fff;
  --line:#b9b9b9;
}
*{box-sizing:border-box;margin:0;padding:0}
html,body{width:1200px;height:2965px;overflow:hidden}
body{position:relative;background:var(--light);font-family:"Alegreya Sans",sans-serif;color:var(--text)}
.abs{position:absolute}

/* header */
.site-header{left:0;top:0;width:1200px;height:100px;background:var(--white)}
.brand{left:100px;top:29px;display:flex;align-items:center;gap:7px}
.brand-mark{width:40px;height:40px;border-radius:50%;border:3px solid var(--darker);background:var(--white);flex:none}
.brand-name{font-size:13px;font-weight:500;color:var(--darker);line-height:1.1;white-space:nowrap}
.main-nav{left:218px;top:44px;display:flex;gap:12px;font-size:13px;letter-spacing:.3px;text-transform:uppercase;color:#8a8a8a;white-space:nowrap}
.main-nav .active{color:var(--orange);border-bottom:1px solid var(--orange);padding-bottom:2px}
.call-btn{background:var(--orange);color:var(--white);display:flex;align-items:center;justify-content:center;gap:12px;font-size:11px;text-transform:uppercase;padding:0 10px;white-space:nowrap}
.call-btn strong{font-size:15px;font-weight:500;letter-spacing:.5px}
.site-header .call-btn{left:918px;top:37px;width:180px;height:31px}

/* hero */
.hero{left:0;top:100px;width:1200px;height:380px;background:linear-gradient(100deg,#4a4a4a 0%,#6a6a6a 45%,#8d8b88 70%,#5a5856 100%)}
.hero-title{left:0;top:148px;width:1200px;text-align:center;color:var(--white);font-weight:300;font-size:38px;letter-spacing:.5px}
.hero-sub{left:0;top:196px;width:1200px;text-align:center;color:var(--white);font-size:13px}
.hero .play{left:570px;top:228px}

.play{width:60px;height:60px}

/* short messages */
.messages{left:0;top:480px;width:1200px;height:142px;display:flex}
.message{flex:1;color:var(--white);text-align:center;font-size:27px;font-weight:500;line-height:1.3;padding-top:34px;text-transform:uppercase}
.message.m1{background:var(--orange)}.message.m2{background:var(--blue)}
.message.m3{background:var(--green)}.message.m4{background:var(--purple)}

/* scenarios */
.scenario{left:0;width:1200px;height:255px}
.scenario .photo{position:absolute;top:0;width:600px;height:255px}
.scenario .panel{position:absolute;top:0;width:600px;height:255px;background:var(--dark);color:#e6e6e6;padding:22px 32px}
.scenario .panel.yellow{background:var(--yellow);color:#3a3320}
.scenario h2{font-weight:300;font-size:31px;text-transform:uppercase;letter-spacing:.3px;color:var(--white);margin-bottom:18px;white-space:nowrap}
.scenario .panel.yellow h2{color:var(--dark)}
.scenario p{font-size:13.5px;line-height:19px;max-width:475px}
.scenario .play{position:absolute;top:98px;left:270px}
.pointer{position:absolute;top:110px;width:0;height:0;border-top:16px solid transparent;border-bottom:16px solid transparent}
.pointer.left{left:-16px;border-right:16px solid var(--dark)}
.pointer.right{right:-16px;border-left:16px solid var(--dark)}
.pointer.right.y{border-left-color:var(--yellow)}

/* bars */
.bars{left:0;top:1642px;width:1200px;height:318px;background:var(--light)}
.bar{position:absolute;width:472px}
.bar h3{font-weight:300;font-size:25px;color:var(--dark);text-transform:uppercase}
.bar .track{height:5px;background:var(--dark);margin-top:10px}
.bar .fill{height:5px}
.bar .pct{font-size:25px;font-weight:700;margin-top:8px}

/* sponsors */
.sponsors{left:0;top:1960px;width:1200px;height:255px;background:var(--dark)}
.sponsors h2{position:absolute;top:50px;width:1200px;text-align:center;color:var(--white);font-weight:300;font-size:38px}
.badge{position:absolute;top:168px;border:2px solid #d8d8d8}

/* contact */
.contact-title{left:0;top:2262px;width:1200px;text-align:center;font-weight:300;font-size:38px;color:var(--dark)}
.contact-sub{left:0;top:2308px;width:1200px;text-align:center;font-size:14px;color:var(--dark)}
.field{position:absolute;border:1px solid #a8a8a8;background:var(--light);font-size:14px;color:#a2a2a2;padding:14px 12px}
.field.filled{color:#555}
.send-btn{left:100px;top:2643px;width:390px;height:48px;background:var(--orange);color:var(--white);font-size:14px;text-transform:uppercase;display:flex;align-items:center;justify-content:center}
.divider{left:600px;top:2445px;width:1px;height:150px;background:#999}
.locations{left:708px;top:2385px;width:390px}
.location-open{height:163px;border:1px solid #a8a8a8;background:var(--light);padding:14px 14px}
.location-open h4{font-weight:400;font-size:16px;color:#777;margin-bottom:20px}
.location-open p{font-size:11.5px;line-height:16px;color:#333}
.location{height:47px;background:var(--darker);color:#ccc;font-size:16px;padding:14px;border-top:1px solid #5a5a5a}

/* footer */
.footer-rule{left:100px;top:2752px;width:998px;height:1px;background:var(--line)}
.footer-brand{left:100px;top:2832px}
.copyright{left:100px;top:2906px;font-size:9.5px;color:#555}
.copyright span{color:var(--orange)}
.sitemap{left:520px;top:2800px;width:130px;text-align:center;font-size:12px;line-height:15px;color:#333}
.footer-heading{font-size:15px;color:#666;margin-bottom:6px}
.sitemap .active{color:var(--orange)}
.posts{left:660px;top:2800px;width:150px;font-size:12px;color:#333}
.posts .footer-heading{text-align:center}
.post{margin-bottom:3px;line-height:14px;white-space:nowrap}
.post small{display:block;font-size:7.5px;color:var(--orange);line-height:8px}
.footer-call{left:873px;top:2803px;width:225px;height:31px}
.social{position:absolute;top:2864px;width:36px;height:36px;border-radius:50%;background:var(--darker)}
.social.orange{background:var(--orange)}
</style>
</head>
<body>

<header class="site-header abs">
  <div class="brand abs"><span class="brand-mark"></span><span class="brand-name">Northgate<br>Health</span></div>
  <nav class="main-nav abs">
    <span>Introduction</span><span>Tobacco Products</span><span>Nicotine Addiction</span><span>Brief Interventions</span><span class="active">Case Scenarios</span><span>Resume</span>
  </nav>
  <div class="call-btn abs">Call us on <strong>02 5550 0192</strong></div>
</header>

<section class="hero abs" role="img" aria-label="Photo of a clenched fist in handcuffs chained to a bundle of cigarettes">
  <h1 class="hero-title abs">LATEST CASE SCENARIO TITLE</h1>
  <p class="hero-sub abs">Some other subtitle</p>
  <svg class="play abs" viewBox="0 0 60 60"><circle cx="30" cy="30" r="26" fill="none" stroke="#f37122" stroke-width="4"/><path d="M24 18 L42 30 L24 42Z" fill="#f37122"/></svg>
</section>

<section class="messages abs">
  <div class="message m1">Short message<br>01</div>
  <div class="message m2">Short message<br>02</div>
  <div class="message m3">Short message<br>03</div>
  <div class="message m4">Short message<br>04</div>
</section>

<article class="scenario abs" style="top:622px">
  <div class="photo" style="left:0;background:linear-gradient(120deg,#8d7f74,#c9b8a8 50%,#6f6660)" role="img" aria-label="Photo of a smoker holding a cigarette beside a name tag">
    <svg class="play" viewBox="0 0 60 60"><circle cx="30" cy="30" r="26" fill="none" stroke="#f37122" stroke-width="4"/><path d="M24 18 L42 30 L24 42Z" fill="#f37122"/></svg>
  </div>
  <div class="panel" style="left:600px">
    <span class="pointer left"></span>
    <h2>Title's link of a C.scenario - 01</h2>
    <p>Dr Hale is one of Australia's most eminent specialists in plastic and cosmetic surgery, and is supported by our highly qualified, professional team. As Sydney's premier plastic surgery clinic, we use only the most revolutionary techniques to minimise scarring to help you look better, feel better and enjoy a beautiful new you. Dr Hale is one of Australia's most eminent specialists in plastic and cosmetic surgery, and is supported by our highly qualified, professional team.</p>
  </div>
</article>

<article class="scenario abs" style="top:877px">
  <div class="panel yellow" style="left:0">
    <span class="pointer right y"></span>
    <h2>Title's link hover..scenario - 02</h2>
    <p>Dr Hale is one of Australia's most eminent specialists in plastic and cosmetic surgery, and is supported by our highly qualified, professional team. As Sydney's premier plastic surgery clinic, we use only the most revolutionary techniques to minimise scarring to help you look better, feel better and enjoy a beautiful new you. Dr Hale is one of Australia's most eminent specialists in plastic and cosmetic surgery, and is supported by our highly qualified, professional team.</p>
  </div>
  <div class="photo" style="left:600px;background:linear-gradient(110deg,#2a2523,#6b5a4f 55%,#3a3330)" role="img" aria-label="Photo of a man lighting a cigarette">
    <svg class="play" viewBox="0 0 60 60"><circle cx="30" cy="30" r="26" fill="none" stroke="#f37122" stroke-width="4"/><path d="M24 18 L42 30 L24 42Z" fill="#f37122"/></svg>
  </div>
</article>

<article class="scenario abs" style="top:1132px">
  <div class="photo" style="left:0;background:linear-gradient(90deg,#0d1a22,#2d6a6a 30%,#2a5a8a 60%,#17304c)" role="img" aria-label="Brain scan images showing activity after nothing, one puff, three puffs, one cigarette and three cigarettes">
    <svg class="play" viewBox="0 0 60 60"><circle cx="30" cy="30" r="26" fill="none" stroke="#f37122" stroke-width="4"/><path d="M24 18 L42 30 L24 42Z" fill="#f37122"/></svg>
  </div>
  <div class="panel" style="left:600px">
    <span class="pointer left"></span>
    <h2>Title's link of a C.scenario - 03</h2>
    <p>Dr Hale is one of Australia's most eminent specialists in plastic and cosmetic surgery, and is supported by our highly qualified, professional team. As Sydney's premier plastic surgery clinic, we use only the most revolutionary techniques to minimise scarring to help you look better, feel better and enjoy a beautiful new you. Dr Hale is one of Australia's most eminent specialists in plastic and cosmetic surgery, and is supported by our highly qualified, professional team.</p>
  </div>
</article>

<article class="scenario abs" style="top:1387px">
  <div class="panel" style="left:0">
    <span class="pointer right"></span>
    <h2>Title's link of a C.scenario - 04</h2>
    <p>Dr Hale is one of Australia's most eminent specialists in plastic and cosmetic surgery, and is supported by our highly qualified, professional team. As Sydney's premier plastic surgery clinic, we use only the most revolutionary techniques to minimise scarring to help you look better, feel better and enjoy a beautiful new you. Dr Hale is one of Australia's most eminent specialists in plastic and cosmetic surgery, and is supported by our highly qualified, professional team.</p>
  </div>
  <div class="photo" style="left:600px;background:linear-gradient(120deg,#3a2518,#6a4a35 45%,#b9b4ae 70%,#4a3020)" role="img" aria-label="Photo of a coffee cup and an ashtray with a cigarette on a wooden table">
    <svg class="play" viewBox="0 0 60 60"><circle cx="30" cy="30" r="26" fill="none" stroke="#f37122" stroke-width="4"/><path d="M24 18 L42 30 L24 42Z" fill="#f37122"/></svg>
  </div>
</article>

<section class="bars abs">
  <div class="bar" style="left:120px;top:65px"><h3>Title for bars 01:</h3><div class="track"><div class="fill" style="width:55%;background:var(--orange)"></div></div><div class="pct" style="color:var(--orange)">55%</div></div>
  <div class="bar" style="left:606px;top:65px"><h3>Title for bars 02:</h3><div class="track"><div class="fill" style="width:70%;background:var(--blue)"></div></div><div class="pct" style="color:var(--blue)">70%</div></div>
  <div class="bar" style="left:120px;top:185px"><h3>Title for bars 03:</h3><div class="track"><div class="fill" style="width:43%;background:var(--green)"></div></div><div class="pct" style="color:var(--green)">47%</div></div>
  <div class="bar" style="left:606px;top:185px"><h3>Title for bars 04:</h3><div class="track"><div class="fill" style="width:93%;background:var(--purple)"></div></div><div class="pct" style="color:var(--purple)">93%</div></div>
</section>

<section class="sponsors abs">
  <h2>SPONSORS</h2>
  <span class="badge" style="left:104px;width:140px;height:48px;border-radius:24px"></span>
  <span class="badge" style="left:310px;width:50px;height:50px;border-radius:50%"></span>
  <span class="badge" style="left:445px;width:130px;height:50px"></span>
  <span class="badge" style="left:660px;width:48px;height:48px;border-radius:50%"></span>
  <span class="badge" style="left:795px;width:70px;height:46px;border-radius:23px"></span>
  <span class="badge" style="left:935px;width:160px;height:50px"></span>
</section>

<h2 class="contact-title abs">CONTACT FORM</h2>
<p class="contact-sub abs">Do write us on our contact form for any details you may be interested on.</p>

<form class="contact-form">
  <div class="field" style="left:100px;top:2385px;width:188px;height:50px">First Name</div>
  <div class="field filled" style="left:302px;top:2385px;width:188px;height:50px">Morgan</div>
  <div class="field" style="left:100px;top:2452px;width:390px;height:50px">Email Address</div>
  <div class="field" style="left:100px;top:2516px;width:390px;height:112px">Message</div>
  <div class="send-btn abs">Send message</div>
</form>

<div class="divider abs"></div>

<div class="locations abs">
  <div class="location-open">
    <h4>Westvale</h4>
    <p>Bellmont Clinic<br>Suite 501<br>12 Rowan Street<br>Westvale 2000</p>
  </div>
  <div class="location">Location 02</div>
  <div class="location">Location 03</div>
  <div class="location">Location 04</div>
</div>

<div class="footer-rule abs"></div>

<footer>
  <div class="brand footer-brand abs"><span class="brand-mark"></span><span class="brand-name">Northgate<br>Health</span></div>
  <p class="copyright abs">© Copyright 2015. <span>Your Company Name</span>. All rights reserved.</p>
  <nav class="sitemap abs">
    <div class="footer-heading">Sitemap</div>
    <div class="active">Introduction</div><div>Tobacco Products</div><div>Nicotine Addiction</div><div>Brief Interventions</div><div>Case Scenarios</div><div>Resume</div>
  </nav>
  <div class="posts abs">
    <div class="footer-heading">Last Posts</div>
    <div class="post">Lorem ipsum dolors met aqui...<small>January 10th, 2015</small></div>
    <div class="post">Lorem ipsum dolors met aqui...<small>January 6th, 2015</small></div>
    <div class="post">Lorem ipsum dolors met aqui...<small>December 12th, 2014</small></div>
  </div>
  <div class="call-btn footer-call abs">Call us on <strong>02 5550 0192</strong></div>
  <span class="social" style="left:904px" aria-label="Social link"></span>
  <span class="social orange" style="left:967px" aria-label="Social link"></span>
  <span class="social" style="left:1030px" aria-label="Social link"></span>
</footer>

</body>
</html>
```